Business card and stationary design for a digital advertising agency

We look to get designs for
- Business card
- Envelope C5 & A4
- Letterhead A4
- Thin Folder (to place the brochures and quotes in. There must be places to put the cd envelope and a business card inside the file as well as a place for the papers)
- CD label & envelope
- Notepad
- Mousepad

We are open for all kind of creativity but please have a look at our website to have an idea. (The website is not ready at the moment but you can see the colours, get the logo, etc.)

Link: www.plexaroth.com/anasayfa

PLEASE NOTE: In the logo file, there are 2 logos but we only use the one on top. We never use the one at the bottom!
Updates

Please use the attached ForDesign.zip file to use the background pattern of our website, inside the folder img there are background patterns of our website. Please use the background or at least inspire from that files in order to design our brochures.  

All designers, please bear in mind that firstly we need the samples of each items described in the brief. Then we will comment on each of them. 

Please submit the designs for all the items at once.

Thanks!

KorvilTek

Target Market(s)

Our customers are the companies who will advertise on internet and digital media and we work mainly in Turkish market

Industry/Entity Type

Digital

Requirements
Must have
• Please use the attached ForDesign.zip file to use the background pattern of our website, inside the folder img there are background patterns of our website. Please use the background or at least inspire from that files in order to design our brochures.
Should not have
• Too much colours such as a child's colouring book.

```html
<!DOCTYPE html>
<html lang="en">
<head>
<meta charset="utf-8">
<title>KorvilTek Stationery – Letterhead and Business Card</title>
<link rel="stylesheet" href="https://fonts.googleapis.com/css2?family=PT+Sans:wght@400;700&display=swap">
<style>
  :root {
    --stage: #e2e2e2;
    --paper: #ffffff;
    --magenta: #c8379a;
    --magenta-dark: #a8267f;
    --ink: #4d4d4d;
    --ink-dark: #222222;
    --brand-grey: #555555;
    --wash-pink: rgba(232, 190, 216, 0.30);
    --wash-green: rgba(214, 230, 190, 0.30);
    --wash-lilac: rgba(210, 212, 236, 0.30);
  }
  * { box-sizing: border-box; margin: 0; padding: 0; }
  html, body { width: 1200px; height: 900px; overflow: hidden; }
  body {
    background: var(--stage);
    font-family: "PT Sans", Arial, sans-serif;
    color: var(--ink);
    position: relative;
  }

  .sheet {
    position: absolute;
    background: var(--paper);
    box-shadow: 0 3px 10px rgba(0,0,0,0.25);
    overflow: hidden;
  }

  .brand-name {
    font-weight: 700;
    color: var(--brand-grey);
    letter-spacing: -0.5px;
    line-height: 1;
  }

  .foot-strip {
    position: absolute; bottom: 0; height: 13px;
    background: linear-gradient(var(--magenta), var(--magenta-dark));
  }

  address { font-style: normal; }

  /* Letterhead */
  .letterhead { left: 61px; top: 26px; width: 598px; height: 847px; }
  .letterhead__top-band { position: absolute; left: 0; top: 0; width: 100%; height: 30px; }
  .letterhead__wash {
    position: absolute; inset: 30px 0 0 0;
    background: linear-gradient(160deg, var(--paper) 0%, var(--wash-pink) 30%, var(--paper) 50%, var(--wash-green) 72%, var(--wash-lilac) 100%);
  }
  .letterhead__brand { position: absolute; left: 28px; top: 38px; font-size: 38px; }
  .letterhead__address {
    position: absolute; left: 0; right: 0; bottom: 8px;
    text-align: center; font-size: 13px; line-height: 17px;
  }
  .letterhead .foot-strip--left { left: 0; width: 135px; }
  .letterhead .foot-strip--right { right: 0; width: 131px; }

  /* Business card */
  .business-card { left: 693px; top: 326px; width: 448px; height: 249px; }
  .business-card__wash {
    position: absolute; inset: 0;
    background: linear-gradient(110deg, var(--wash-lilac) 0%, var(--wash-pink) 15%, var(--wash-green) 28%, var(--paper) 55%, var(--paper) 100%);
  }
  .business-card__brand { position: absolute; right: 30px; top: 26px; font-size: 34px; }
  .business-card__person {
    position: absolute; left: 256px; top: 116px; width: 130px; text-align: center;
  }
  .person-name {
    font-size: 18px; font-weight: 700; color: var(--ink-dark);
    padding-bottom: 1px; border-bottom: 1.5px solid var(--ink-dark);
  }
  .person-role { font-size: 11.5px; color: var(--ink-dark); margin-top: 8px; }
  .business-card__address {
    position: absolute; right: 13px; top: 212px;
    text-align: right; font-size: 11.5px; line-height: 17px;
  }
  .business-card .foot-strip--left { left: 0; width: 167px; }
</style>
</head>
<body>

<section class="sheet letterhead" aria-label="Letterhead">
  <svg class="letterhead__top-band" viewBox="0 0 598 30" preserveAspectRatio="none" aria-hidden="true">
    <polygon points="0,0 598,0 598,28 586,15 12,15 0,28" fill="#c8379a"/>
  </svg>
  <div class="letterhead__wash" role="img" aria-label="Faint pastel background pattern in pink, green and lilac tones"></div>
  <p class="brand-name letterhead__brand">KorvilTek</p>
  <address class="letterhead__address">
    Akçay Caddesi, Lale Mahallesi, No: 48 Kat:3&nbsp; Levent, İstanbul<br>
    Tel: +90 212 555 01 42, E-mail: info@korviltek.com
  </address>
  <div class="foot-strip foot-strip--left"></div>
  <div class="foot-strip foot-strip--right"></div>
</section>

<section class="sheet business-card" aria-label="Business card">
  <div class="business-card__wash" role="img" aria-label="Faint pastel background pattern in lilac, pink and green tones"></div>
  <p class="brand-name business-card__brand">KorvilTek</p>
  <div class="business-card__person">
    <p class="person-name">elin marsk</p>
    <p class="person-role">Branch Manager</p>
  </div>
  <address class="business-card__address">
    Akçay Caddesi, Lale Mahallesi, No: 48 Kat:3&nbsp; Levent, İstanbul<br>
    Tel: +90 212 555 01 42, E-mail: info@korviltek.com
  </address>
  <div class="foot-strip foot-strip--left"></div>
</section>

</body>
</html>
```